Change consultancy needs business card+ design

We need business card design for a Seattle based consulting firm called
Harlow + Dunmore. Our firm helps organizations shift their paradigms, lean into change, and reimagine the way they work together.
**Updated**
Our firm name is the logo using black and orange font, see attached. We would like to include the tagline "(Re)imagining how people work"
The final design should find a balance between playful, edgy and professional. For example, we are using the attached goldfish photo on our homepage and like the colors and concept of leaping forward. However, don't want to use the image on the card.
Lastly, depending on the winning design, we will also be looking for stationary/template design that will compliment the business card.
- Helvetica

```html
<!DOCTYPE html>
<html lang="en">
<head>
<meta charset="utf-8">
<title>Harlow + Dunmore business card</title>
<link rel="stylesheet" href="https://fonts.googleapis.com/css2?family=Open+Sans:wght@400;500&display=swap">
<style>
  :root {
    --backdrop: #c9c9c9;
    --paper: #fafafa;
    --brand-ink: #1a1a1a;
    --tagline-ink: #4a4a4a;
    --card-blue-top: #10b0e0;
    --card-blue-bottom: #0399d6;
    --accent-orange: #e8891c;
    --edge-orange: #d98a2a;
    --ink-white: #ffffff;
  }
  * { margin: 0; padding: 0; box-sizing: border-box; }
  html, body {
    width: 1200px;
    height: 720px;
    overflow: hidden;
    background: var(--backdrop);
    font-family: "Open Sans", Arial, sans-serif;
  }
  .canvas {
    position: relative;
    width: 1200px;
    height: 720px;
    display: flex;
    align-items: center;
    justify-content: center;
    gap: 60px;
  }
  .card {
    position: relative;
    width: 520px;
    height: 297px;
    border: 2px solid var(--edge-orange);
    box-shadow: 0 2px 6px rgba(0,0,0,0.12);
    overflow: hidden;
  }
  .card--front {
    background: var(--paper);
    display: flex;
    flex-direction: column;
    align-items: center;
    justify-content: center;
    gap: 12px;
  }
  .brand-lockup {
    display: flex;
    align-items: center;
    gap: 12px;
  }
  .brand-square {
    width: 16px;
    height: 16px;
    background: var(--accent-orange);
    flex: none;
  }
  .brand-name {
    font-weight: 500;
    font-size: 34px;
    line-height: 1;
    white-space: nowrap;
    color: var(--brand-ink);
  }
  .tagline {
    font-size: 14px;
    font-weight: 400;
    letter-spacing: 0.4px;
    color: var(--tagline-ink);
  }
  .card--back {
    background: linear-gradient(160deg, var(--card-blue-top), var(--card-blue-bottom));
    color: var(--ink-white);
  }
  .back-marker {
    position: absolute;
    left: 56px;
    top: 98px;
    width: 16px;
    height: 16px;
    background: var(--accent-orange);
  }
  .holder {
    position: absolute;
    left: 92px;
    top: 88px;
    display: flex;
    align-items: baseline;
    gap: 12px;
  }
  .holder-name {
    font-size: 21px;
    font-weight: 400;
  }
  .holder-title {
    font-size: 12px;
    letter-spacing: 0.6px;
    text-transform: uppercase;
  }
  .contact-lines {
    position: absolute;
    left: 120px;
    top: 140px;
    list-style: none;
    font-size: 12.5px;
    line-height: 19px;
  }
  .contact-lines li { display: flex; gap: 14px; }
  .contact-label {
    width: 10px;
    color: var(--accent-orange);
  }
  .postal-address {
    position: absolute;
    left: 144px;
    top: 212px;
    font-style: normal;
    font-size: 12.5px;
    line-height: 19px;
  }
  .web-address {
    position: absolute;
    left: 144px;
    top: 256px;
    font-size: 12.5px;
  }
</style>
</head>
<body>
  <main class="canvas">
    <section class="card card--front" aria-label="Card front">
      <div class="brand-lockup">
        <span class="brand-square" aria-hidden="true"></span>
        <span class="brand-name">Harlow + Dunmore, LLC</span>
      </div>
      <p class="tagline">(Re)imagining how people work</p>
    </section>

    <section class="card card--back" aria-label="Card back">
      <span class="back-marker" aria-hidden="true"></span>
      <div class="holder">
        <span class="holder-name">Nadia Whitcombe</span>
        <span class="holder-title">Principal</span>
      </div>
      <ul class="contact-lines">
        <li><span class="contact-label">T</span><span>206-555-0148</span></li>
        <li><span class="contact-label">M</span><span>206-555-0192</span></li>
        <li><span class="contact-label">E</span><span>whitcombe@harlow_dunmore.com</span></li>
      </ul>
      <address class="postal-address">
        418 Pinecrest Avenue, Suite 7B<br>
        Seattle, Washington 98104
      </address>
      <div class="web-address">www.harlow_dunmore.com</div>
    </section>
  </main>
</body>
</html>
```